Social Media Graphics - Harbor Climb REVISED

Create 6-7 individual social media graphics (square size) to encourage folks to join our online course called:

The Lantern Ledger Plan
How to Launch a Multi-Million Business From Scratch
Sign Up Today!

IMPORTANT: Make the largest and most prominent text on the graphic be: How to Launch a Multi-Million Business From Scratch

For the color scheme of the graphics, let's try a blue color palette; make sure the graphics appeal to both men and women

Make sure each graphic contains 1 of the 3 pics attached (crop pic as needed); and make sure one of the graphics is all TEXT only.

Target Market(s)

men and women looking to start a business

Industry/Entity Type

Entrepreneurship

Colors
0054AA
0677BA
7BADD7
CADEEF
E8F1F8

Requirements
Must have
• All the text and use the 3 pics provided; one graphic can be all text; Simple, modern design that's easy to read

```html
<!DOCTYPE html>
<html lang="en">
<head>
<meta charset="utf-8">
<title>The Lantern Ledger Plan – Social Graphics</title>
<link href="https://fonts.googleapis.com/css2?family=Krona+One&family=Yellowtail&family=Great+Vibes&display=swap" rel="stylesheet">
<style>
  :root {
    --board: #a3a3a3;
    --royal: #0054aa;
    --ocean: #0677ba;
    --sky: #7badd7;
    --mist: #cadeef;
    --frost: #e8f1f8;
    --deep: #0d5590;
    --white: #ffffff;
    --wide: "Krona One", sans-serif;
    --script: "Yellowtail", cursive;
    --flourish: "Great Vibes", cursive;
  }
  * { margin: 0; padding: 0; box-sizing: border-box; }
  html, body { width: 1189px; height: 1200px; overflow: hidden; }
  body { background: var(--board); position: relative; font-family: var(--wide); color: var(--white); }

  .tile { position: absolute; width: 519px; height: 519px; overflow: hidden; box-shadow: 0 6px 18px rgba(0,0,0,.25); }
  .tile--a { left: 52px; top: 59px; background: linear-gradient(180deg, #92b9d8 0%, #2f75ab 30%, #155f99 60%, #0c5189 100%); }
  .tile--b { left: 617px; top: 59px; background: radial-gradient(circle at 8% 40%, #7fb0de 0%, #2f74c4 35%, #1e66bc 100%); }
  .tile--c { left: 52px; top: 622px; background: linear-gradient(200deg, #4d8fc0 0%, #1d6aa6 35%, #155f9b 70%, #3b80b4 100%); }
  .tile--d { left: 617px; top: 622px; background: linear-gradient(225deg, #82b3d7 0%, #1a64a0 30%, #135c98 60%, #4a8aba 75%, #0f5690 100%); }

  .abs { position: absolute; }
  .center { left: 0; right: 0; text-align: center; white-space: nowrap; }
  .photo { position: absolute; }

  /* tile A */
  .ghost-word { top: 56px; font-size: 58px; color: rgba(160,195,225,.28); letter-spacing: 2px; }
  .tile--a .photo { left: 80px; top: 18px; width: 360px; height: 290px; border-radius: 140px 140px 20px 20px;
    background: linear-gradient(180deg, rgba(40,55,80,.55), rgba(20,60,110,.35)); }
  .tile--a .script-title { top: 262px; font-family: var(--script); font-size: 34px; color: #9ec2e2; }
  .tile--a .main-title { top: 308px; font-size: 37px; }
  .pill { left: 24px; top: 370px; width: 472px; height: 71px; border-radius: 36px; background: var(--ocean);
    display: flex; align-items: center; justify-content: center; text-align: center; font-size: 15px; line-height: 23px; }
  .tile--a .flourish-cta { top: 455px; font-family: var(--flourish); font-size: 32px; }

  /* tile B */
  .tile--b .head-line { top: 22px; font-size: 33px; }
  .title-box { left: 68px; top: 69px; width: 384px; height: 51px; background: var(--ocean); border-radius: 3px;
    display: flex; align-items: center; justify-content: center; font-size: 33px; white-space: nowrap; }
  .tile--b .photo { left: 90px; top: 150px; width: 340px; height: 369px; border-radius: 150px 150px 0 0;
    background: linear-gradient(180deg, rgba(30,30,40,.45) 0%, rgba(200,40,70,.45) 55%, rgba(25,25,30,.55) 100%); }
  .side-tab { left: 472px; top: 163px; width: 47px; height: 225px; background: var(--ocean); border-radius: 8px 0 0 8px;
    display: flex; align-items: center; justify-content: center; }
  .side-tab span { transform: rotate(-90deg); white-space: nowrap; font-size: 14px; }
  .band { left: 0; top: 428px; width: 519px; height: 72px; background: var(--mist); color: var(--deep);
    display: flex; align-items: center; justify-content: center; text-align: center; font-size: 17px; line-height: 25px; }

  /* tile C */
  .tile--c .head-line { font-size: 36px; color: var(--mist); }
  .tile--c .head-one { top: 26px; }
  .tile--c .head-two { top: 78px; font-size: 37px; }
  .tile--c .side-block { left: 0; top: 262px; width: 42px; height: 257px; background: #52a6e2; }
  .tile--c .photo { left: 10px; top: 112px; width: 350px; height: 407px; border-radius: 90px 90px 0 0;
    background: linear-gradient(180deg, rgba(40,40,50,.35), rgba(160,160,165,.35) 50%, rgba(20,20,25,.5)); }
  .stack-text { left: 361px; top: 193px; font-size: 17.5px; line-height: 27px; }
  .tab-btn { left: 296px; top: 418px; width: 201px; height: 48px; background: var(--ocean); border-radius: 0 24px 24px 0;
    display: flex; align-items: center; justify-content: center; font-size: 13px; }

  /* tile D */
  .tile--d .script-title { top: 40px; font-family: var(--script); font-size: 50px; }
  .outline-title { top: 110px; font-size: 36px; color: transparent; -webkit-text-stroke: 1.6px var(--white); }
  .big-lines { top: 200px; font-size: 27px; line-height: 45px; }
  .round-btn { left: 141px; top: 421px; width: 237px; height: 48px; background: var(--ocean); border-radius: 24px;
    display: flex; align-items: center; justify-content: center; font-size: 14px; }
</style>
</head>
<body>

  <section class="tile tile--a">
    <div class="abs center ghost-word">LEDGER</div>
    <div class="photo" role="img" aria-label="Photo of the two course hosts standing together, arms crossed, smiling"></div>
    <div class="abs center script-title">The Lantern</div>
    <div class="abs center main-title">LEDGER PLAN</div>
    <div class="abs pill">HOW TO LAUNCH A MULTI-MILLION<br>BUSINESS FROM SCRATCH</div>
    <div class="abs center flourish-cta">Sign Up Today!</div>
  </section>

  <section class="tile tile--b">
    <div class="abs center head-line">THE LANTERN</div>
    <div class="abs title-box">LEDGER PLAN</div>
    <div class="photo" role="img" aria-label="Photo of the two course hosts, she in a red dress and he in black, smiling"></div>
    <div class="abs side-tab"><span>SIGN UP TODAY!</span></div>
    <div class="abs band">HOW TO LAUNCH A MULTI-MILLION<br>BUSINESS FROM SCRATCH</div>
  </section>

  <section class="tile tile--c">
    <div class="abs side-block"></div>
    <div class="photo" role="img" aria-label="Photo of the two hosts on stage, one speaking into a microphone"></div>
    <div class="abs center head-line head-one">THE LANTERN</div>
    <div class="abs center head-line head-two">LEDGER PLAN</div>
    <div class="abs stack-text">HOW TO<br>LAUNCH A<br>MULTI-<br>MILLION<br>BUSINESS<br>FROM<br>SCRATCH</div>
    <div class="abs tab-btn">SIGN UP TODAY!</div>
  </section>

  <section class="tile tile--d">
    <div class="abs center script-title">The Lantern</div>
    <div class="abs center outline-title">LEDGER PLAN</div>
    <div class="abs center big-lines">HOW TO LAUNCH A<br>MULTI-MILLION<br>BUSINESS FROM<br>SCRATCH</div>
    <div class="abs round-btn">SIGN UP TODAY!</div>
  </section>

</body>
</html>
```